An Annual event hosted by The Kelvaro Heritage Society of New South Wales. The event is called ZUMIRA Night Red Carpet Event.

The event will be on Saturday 22th November 2014, from 4pm at Halbrook Centre, 47 Larkin Rd, Denvale NSW 2961.

Guests will be entertained by a live band led by
Mr. Gerald with Tembu Group and legendary DJ Vek will deliver the best African tune!

Various people from different culture will be welcomed to dine and dance with the community for ONLY $10.

Guests are required to dress to impress for Professional Photographs in Style on our Red Carpet Entry.

We need to notify our Guests that the entry fee will cover East African Food and Soft drinks to support The Kelvaro Heritage Society of New South Wales.

The event is for everyone including family and friends.

RSVP can be made to the Secretary, Mr Harold Besk on 0497302861 or to the Chair, Mr Dennis Kolvu on 0496718203 by Monday 17 November 2014.

The poster need to be unique, attractive with bright colours and at the same time reflecting the nature of a red carpet event including Red carpet, bollards and shiny lights.

We need the poster to include text and graphics design.

Please note the community currently does not have a logo instead we are using two flags i.e. Tanzania and Australia flags and would like the flags to appear on the poster as well.

Families from different nationalities.

Church

• The poster must reflect a red carpet theme....

```html
<!DOCTYPE html>
<html lang="en">
<head>
<meta charset="utf-8">
<title>ZUMIRA Night Red Carpet Event</title>
<link rel="stylesheet" href="https://fonts.googleapis.com/css2?family=Russo+One&family=Oswald:wght@400;600;700&family=Great+Vibes&display=swap">
<style>
:root{
  --navy:#061238;
  --deep:#0a1f5c;
  --blue:#1b4fb8;
  --sky:#5fa8f0;
  --red:#d3121a;
  --red-dark:#8e0a10;
  --yellow:#ffd21a;
  --white:#ffffff;
  --silver:#dfe6f2;
  --green:#1eb53a;
}
*{margin:0;padding:0;box-sizing:border-box}
html,body{width:847px;height:1200px;overflow:hidden;background:var(--navy)}
.poster{position:relative;width:847px;height:1200px;overflow:hidden;
  background:radial-gradient(ellipse at 50% 62%,#1d4db5 0%,var(--deep) 45%,var(--navy) 80%);
  font-family:'Oswald',sans-serif;color:var(--white);text-align:center}
.presenter-band{position:absolute;top:0;left:0;right:0;height:46px;background:var(--red);
  display:flex;align-items:center;justify-content:center;font-weight:600;font-size:21px;letter-spacing:.5px;z-index:3}
.flag-left{position:absolute;top:46px;left:0;width:440px;height:300px;
  background:linear-gradient(160deg,#1a3a9e,#0b1f6a)}
.flag-right{position:absolute;top:110px;right:0;width:380px;height:250px;
  background:linear-gradient(150deg,var(--green) 0 38%,#000 38% 52%,#12a6de 52%)}
.hero-photo{position:absolute;top:46px;left:250px;width:340px;height:420px;
  background:linear-gradient(180deg,#3a2a22 0%,#6b4a3a 40%,#e8e8ee 75%,rgba(255,255,255,0) 100%);
  border-radius:40% 40% 10% 10%;z-index:1}
.date-badge{position:absolute;top:60px;left:175px;width:190px;height:190px;border-radius:50%;
  background:radial-gradient(circle,#ee2a2f,var(--red-dark));border:5px solid var(--white);
  display:flex;flex-direction:column;align-items:center;justify-content:center;z-index:2;line-height:1}
.date-badge .day{font-weight:700;font-size:22px}
.date-badge .num{font-family:'Russo One',sans-serif;font-size:64px}
.date-badge .num sup{font-size:22px}
.date-badge .month{font-weight:700;font-size:22px}
.date-badge .doors{font-size:13px;margin-top:4px}
.title{position:absolute;top:500px;left:0;right:0;font-family:'Russo One',sans-serif;line-height:.9;z-index:2;
  background:linear-gradient(180deg,var(--white) 0%,var(--silver) 50%,#8fa0bf 52%,var(--white) 100%);
  -webkit-background-clip:text;background-clip:text;color:transparent;
  filter:drop-shadow(0 0 14px rgba(120,180,255,.8))}
.title .line1{display:block;font-size:150px;letter-spacing:4px}
.title .line2{display:block;font-size:110px;letter-spacing:6px;opacity:.85}
.event-band{position:absolute;top:742px;left:140px;right:140px;height:54px;
  background:linear-gradient(180deg,#ef2b30,var(--red-dark));font-family:'Russo One',sans-serif;
  font-size:40px;line-height:54px;z-index:2}
.bollard{position:absolute;top:700px;width:24px;height:110px;border-radius:12px 12px 4px 4px;
  background:linear-gradient(90deg,#8a7a3a,#f4dd8a,#8a7a3a)}
.bollard.left{left:70px}.bollard.right{right:70px}
.info{position:absolute;top:808px;left:0;right:0;line-height:1.1;z-index:2}
.live{font-family:'Russo One',sans-serif;font-size:30px}
.band{font-family:'Russo One',sans-serif;font-size:40px}
.band em{font-style:normal;font-family:'Oswald',sans-serif;font-size:30px}
.dj{color:var(--yellow);font-weight:700;font-size:38px;margin-top:4px}
.dress{font-size:21px;font-weight:600}
.fee{color:var(--yellow);font-size:22px;font-weight:600;line-height:1.15}
.venue{margin-top:10px;font-family:'Russo One',sans-serif;font-size:52px;line-height:1}
.venue .at{font-family:'Great Vibes',cursive;font-size:60px;color:var(--yellow)}
.address{font-weight:700;font-size:26px}
.welcome{font-size:21px;line-height:1.2;margin-top:4px}
.rsvp-band{position:absolute;bottom:0;left:0;right:0;height:34px;background:var(--red);
  font-size:17px;line-height:34px;font-weight:600}
</style>
</head>
<body>
<div class="poster">
  <div class="presenter-band">THE KELVARO HERITAGE SOCIETY OF NEW SOUTH WALES PRESENTS</div>
  <div class="flag-left" role="img" aria-label="Waving Australian flag"></div>
  <div class="flag-right" role="img" aria-label="Waving Tanzanian flag"></div>
  <div class="hero-photo" role="img" aria-label="Photo of a woman in a white dress posing"></div>
  <div class="date-badge">
    <span class="day">SATURDAY</span>
    <span class="num">22<sup>ND</sup></span>
    <span class="month">NOVEMBER</span>
    <span class="doors">DOORS OPEN 4PM TILL LATE</span>
  </div>
  <div class="bollard left"></div>
  <div class="bollard right"></div>
  <h1 class="title"><span class="line1">ZUMIRA</span><span class="line2">NIGHT</span></h1>
  <div class="event-band">RED CARPET EVENT</div>
  <div class="info">
    <div class="live">LIVE BAND ENTERTAINMENT BY</div>
    <div class="band">MR. GERALD <em>with</em> TEMBU GROUP</div>
    <div class="dj">BEST AFRICAN TUNE WITH LEGENDARY DJ VEK</div>
    <div class="dress">DRESS TO IMPRESS FOR PROFESSIONAL PHOTOS IN STYLE ON RED CARPET ENTRY</div>
    <div class="fee">ENTRY FEE WILL COVER EAST AFRICAN FOOD &amp; SOFT DRINKS TO SUPPORT<br>THE KELVARO HERITAGE SOCIETY OF NEW SOUTH WALES</div>
    <div class="venue"><span class="at">At</span> HALBROOK CENTRE</div>
    <div class="address">47 LARKIN RD, DENVALE NSW 2961</div>
    <div class="welcome">VARIOUS PEOPLE FROM DIFFERENT CULTURE ARE WELCOMED<br>TO DINE AND DANCE WITH THE COMMUNITY FOR ONLY $10</div>
  </div>
  <div class="rsvp-band">RSVP BY MONDAY 17 NOVEMBER 2014 CONTACT SECRETARY: MR HAROLD BESK 0497302861 / CHAIRMAN: MR DENNIS KOLVU 0496718203</div>
</div>
</body>
</html>
```